R J Security Flyer - Security Based Company

Security company offering installation of CCTV and Intruder alarm systems mainly but not limited to home alarms. Feel free to be creative

Target Market(s)

Residential and Commercial properties, Facility Managers, local business

Requirements
Must have
• smart professional finish, logo and latest up to date pictures if on kit

```html
<!DOCTYPE html>
<html lang="en">
<head>
<meta charset="utf-8">
<title>R J Security Flyer - Security Based Company</title>
<link href="https://fonts.googleapis.com/css2?family=Rajdhani:wght@400;500;600;700&family=Roboto:wght@300;400&display=swap" rel="stylesheet">
<style>
  :root {
    --orange: #f15a22;
    --black: #0b0b0b;
    --ink: #1c1c1c;
    --board: #58595b;
    --white: #ffffff;
    --rule: #c9c9c9;
    --label: #f7941d;
  }
  * { box-sizing: border-box; margin: 0; padding: 0; }
  html, body { width: 1200px; height: 897px; overflow: hidden; }
  body { background: var(--board); font-family: "Rajdhani", sans-serif; color: var(--ink); position: relative; }

  .flyer { position: absolute; top: 53px; width: 500px; height: 713px; background: var(--white); overflow: hidden; box-shadow: 0 10px 18px rgba(0,0,0,.35); }
  .flyer--front { left: 82px; }
  .flyer--back { left: 646px; }

  .side-label { position: absolute; top: 792px; font-family: "Roboto", sans-serif; font-weight: 300; font-size: 20px; color: var(--label); }
  .side-label--front { left: 80px; }
  .side-label--back { left: 644px; }
  .board-caption { position: absolute; top: 830px; left: 0; width: 1200px; text-align: center; font-family: "Roboto", sans-serif; font-weight: 300; font-size: 29px; color: var(--white); letter-spacing: .5px; }

  .brand { position: absolute; left: 23px; top: 30px; width: 180px; text-align: center; }
  .brand__mark { display: block; width: 38px; height: 38px; margin: 0 auto 10px; background: var(--orange); border-radius: 50%; }
  .brand__name { font-weight: 700; font-size: 28px; line-height: 1; color: var(--orange); letter-spacing: .3px; }
  .brand__sub { display: flex; align-items: center; justify-content: center; gap: 5px; margin-top: 6px; font-size: 17px; font-weight: 500; letter-spacing: 2px; color: var(--orange); }
  .brand__sub::before, .brand__sub::after { content: ""; width: 34px; height: 2px; background: var(--orange); }

  .headline { position: absolute; left: 26px; top: 150px; }
  .headline__lead { font-size: 24px; font-weight: 500; line-height: 26px; color: var(--ink); }
  .headline__key { font-size: 40px; font-weight: 700; line-height: 38px; color: var(--orange); margin-top: 4px; }

  .checks { position: absolute; left: 26px; top: 296px; width: 268px; list-style: none; }
  .checks li { position: relative; padding: 0 0 6px 26px; margin-bottom: 6px; font-size: 10.6px; font-weight: 500; line-height: 14.3px; border-bottom: 1px solid var(--rule); }
  .checks li:last-child { border-bottom: none; }
  .tick { position: absolute; left: 8px; top: 1px; width: 13px; height: 13px; }

  .photo { position: absolute; }
  .photo svg { width: 100%; height: 100%; display: block; }

  .quote-band { position: absolute; left: 0; top: 594px; width: 314px; height: 61px; background: var(--orange); clip-path: polygon(0 0, 285px 0, 314px 61px, 0 61px); color: var(--white); padding: 7px 0 0 18px; }
  .quote-band__text { font-size: 9.6px; font-weight: 500; line-height: 16px; }
  .quote-band__cta { font-size: 19px; font-weight: 700; line-height: 20px; }

  .listing-mark { position: absolute; left: 312px; top: 621px; width: 110px; height: 22px; background: #e8e8e8; border-radius: 3px; }
  .cert-mark { position: absolute; left: 436px; top: 595px; width: 34px; height: 34px; border-radius: 50%; border: 2px solid #1e3c7d; background: #eef1f7; }

  .contact-bar { position: absolute; left: 0; top: 655px; width: 500px; height: 58px; background: var(--black); color: var(--white); }
  .contact-bar__icon { position: absolute; left: 22px; top: 19px; width: 20px; height: 20px; border-radius: 50%; background: var(--orange); }
  .contact-bar__icon svg { width: 20px; height: 20px; }
  .contact-bar__phone { position: absolute; left: 48px; top: 9px; width: 214px; font-size: 35px; font-weight: 700; line-height: 40px; letter-spacing: 0; white-space: nowrap; }
  .contact-bar__details { position: absolute; left: 274px; top: 10px; list-style: none; font-size: 9.4px; line-height: 13px; font-weight: 500; white-space: nowrap; }
  .contact-bar__details li { position: relative; padding-left: 12px; }
  .contact-bar__details li::before { content: ""; position: absolute; left: 1px; top: 4px; width: 6px; height: 6px; border-radius: 50%; background: var(--orange); }

  .back-title { position: absolute; top: 22px; left: 0; width: 500px; text-align: center; font-size: 28px; font-weight: 700; color: var(--orange); line-height: 30px; letter-spacing: .3px; }
  .back-intro { position: absolute; top: 52px; left: 0; width: 500px; text-align: center; font-size: 17.5px; font-weight: 500; line-height: 23px; }

  .benefits { position: absolute; left: 30px; top: 134px; width: 440px; height: 204px; border: 1.5px solid var(--orange); border-radius: 12px; }
  .benefits__tab { position: absolute; left: 127px; top: -25px; width: 188px; height: 46px; background: var(--black); clip-path: polygon(14px 0, 174px 0, 188px 23px, 174px 46px, 14px 46px, 0 23px); text-align: center; line-height: 18px; padding-top: 5px; font-size: 17px; }
  .benefits__tab-top { color: var(--white); font-weight: 500; }
  .benefits__tab-key { color: var(--orange); font-weight: 700; }
  .benefits__list { position: absolute; left: 0; top: 32px; list-style: none; }
  .benefits__list li { position: relative; padding-left: 28px; font-size: 11.6px; font-weight: 500; line-height: 15px; margin-bottom: 6.7px; width: 430px; }
  .benefits__list .tick { left: 9px; }

  .hex-row { position: absolute; top: 358px; left: 0; width: 500px; height: 130px; }
  .hex-row .photo { width: 116px; height: 132px; top: 0; }
  .hex-shadow { position: absolute; top: 143px; width: 90px; height: 8px; border-radius: 50%; background: radial-gradient(rgba(0,0,0,.18), rgba(0,0,0,0) 70%); }

  .back-body { position: absolute; top: 518px; left: 28px; width: 444px; text-align: center; font-size: 10.6px; font-weight: 500; line-height: 14.4px; }

  .promise-band { position: absolute; top: 595px; left: 0; width: 500px; height: 60px; background: var(--orange); color: var(--white); text-align: center; font-size: 19px; font-weight: 700; line-height: 23px; padding-top: 7px; }
</style>
</head>
<body>

<svg width="0" height="0" style="position:absolute">
  <defs>
    <symbol id="tick-box" viewBox="0 0 14 14">
      <rect x="1" y="3" width="10" height="10" fill="none" stroke="#f15a22" stroke-width="1.4"/>
      <path d="M3.5 7.5 L6 10 L13 1.5" fill="none" stroke="#f15a22" stroke-width="1.8"/>
    </symbol>
    <linearGradient id="g-camera" x1="0" y1="0" x2="1" y2="1"><stop offset="0" stop-color="#c9c4bb"/><stop offset=".5" stop-color="#6f6c68"/><stop offset="1" stop-color="#b8b2a8"/></linearGradient>
    <linearGradient id="g-phone" x1="0" y1="0" x2="1" y2="1"><stop offset="0" stop-color="#5a4a3e"/><stop offset=".55" stop-color="#3d6f86"/><stop offset="1" stop-color="#c9a47e"/></linearGradient>
    <linearGradient id="g-keypad" x1="0" y1="0" x2="1" y2="1"><stop offset="0" stop-color="#e4e6ea"/><stop offset=".5" stop-color="#8a95a6"/><stop offset="1" stop-color="#d6d8dc"/></linearGradient>
    <linearGradient id="g-app" x1="0" y1="0" x2="1" y2="1"><stop offset="0" stop-color="#f4f6f8"/><stop offset=".5" stop-color="#2e8fd6"/><stop offset="1" stop-color="#e9ecef"/></linearGradient>
  </defs>
</svg>

<section class="flyer flyer--front">
  <div class="brand">
    <span class="brand__mark"></span>
    <div class="brand__name">R J SECURITY</div>
    <div class="brand__sub">SYSTEMS</div>
  </div>

  <div class="headline">
    <p class="headline__lead">Are You Looking To<br>Keep You Or Your</p>
    <p class="headline__key">PREMISES<br>SAFE?</p>
  </div>

  <ul class="checks">
    <li><svg class="tick"><use href="#tick-box"/></svg>We install, maintain and repair all intruder alarms, CCTV, intercom and access control</li>
    <li><svg class="tick"><use href="#tick-box"/></svg>View, control and manage your security systems anywhere in the world with smartphone apps</li>
    <li><svg class="tick"><use href="#tick-box"/></svg>Feel at ease with monitoring services and police response tailored to suit you and your business</li>
    <li><svg class="tick"><use href="#tick-box"/></svg>We can takeover any existing security system and offer maintenance checks to guarantee the best performance for you and your premises</li>
    <li><svg class="tick"><use href="#tick-box"/></svg>We understand that being security conscious is ever increasing, protecting your property and family is a number one priority</li>
    <li><svg class="tick"><use href="#tick-box"/></svg>Our fully insured and accredited team offer quality, safety and cost efficiency throughout and whole process</li>
  </ul>

  <div class="photo" style="left:236px;top:0;width:264px;height:270px" role="img" aria-label="Photo of a wall-mounted CCTV security camera">
    <svg viewBox="0 0 264 270">
      <polygon points="62,0 264,0 264,215 130,266 4,218 4,100" fill="#111"/>
      <polygon points="66,0 264,0 264,205 130,254 14,212 14,102" fill="url(#g-camera)"/>
      <polyline points="4,215 4,98 60,0" fill="none" stroke="#f15a22" stroke-width="9"/>
    </svg>
  </div>

  <div class="photo" style="left:324px;top:238px;width:160px;height:170px" role="img" aria-label="Photo of a hand holding a smartphone running a security app">
    <svg viewBox="0 0 160 170">
      <polygon points="80,3 157,45 157,125 80,167 3,125 3,45" fill="url(#g-phone)" stroke="#111" stroke-width="5"/>
      <polyline points="3,70 3,45 80,3 157,45 157,70" fill="none" stroke="#f15a22" stroke-width="6"/>
    </svg>
  </div>

  <div class="photo" style="left:324px;top:390px;width:160px;height:180px" role="img" aria-label="Photo of an intruder alarm keypad on a wall">
    <svg viewBox="0 0 160 180">
      <polygon points="80,3 157,47 157,133 80,177 3,133 3,47" fill="url(#g-keypad)" stroke="#111" stroke-width="5"/>
      <polyline points="3,72 3,47 80,3 157,47 157,72" fill="none" stroke="#f15a22" stroke-width="6"/>
    </svg>
  </div>

  <div class="quote-band">
    <p class="quote-band__text">If you are looking to improve the security in your home,<br>office or commercial property then call a member of our team</p>
    <p class="quote-band__cta">Today for a free quote.</p>
  </div>
  <span class="listing-mark"></span>
  <span class="cert-mark"></span>

  <div class="contact-bar">
    <span class="contact-bar__icon"><svg viewBox="0 0 20 20"><path d="M12.5 5.5c-2.5-.5-5 1.8-5 4.5s2.5 5 5 4.5l-.6-2.4c-1.2.1-2.1-.9-2.1-2.1s.9-2.2 2.1-2.1z" fill="#fff"/></svg></span>
    <p class="contact-bar__phone">01632 960482</p>
    <ul class="contact-bar__details">
      <li>14 Harbour Lane, Marston, Essex, CM99 2ZX</li>
      <li>operations@rjsecuritysystems.co.uk</li>
      <li>www.rjsecuritysystems.co.uk</li>
    </ul>
  </div>
</section>

<section class="flyer flyer--back">
  <h1 class="back-title">R J SECURITY SYSTEMS</h1>
  <p class="back-intro">are using the latest cloud-based technology to stay<br>connected with your home and business 24/7.</p>

  <div class="benefits">
    <div class="benefits__tab"><div class="benefits__tab-top">Some Benefits of</div><div class="benefits__tab-key">Cloud Services Are</div></div>
    <ul class="benefits__list">
      <li><svg class="tick"><use href="#tick-box"/></svg>High level support 24/7</li>
      <li><svg class="tick"><use href="#tick-box"/></svg>Reduce engineer call outs and running costs</li>
      <li><svg class="tick"><use href="#tick-box"/></svg>Identify issues in advance</li>
      <li><svg class="tick"><use href="#tick-box"/></svg>Remotely manage systems to ensure correct operation</li>
      <li><svg class="tick"><use href="#tick-box"/></svg>Remote health checks carried out to keep your system performing as it should</li>
      <li><svg class="tick"><use href="#tick-box"/></svg>Automatically update your system with the latest releases via cloud<br>application software</li>
      <li><svg class="tick"><use href="#tick-box"/></svg>Interact, control and integrate your security system like never before</li>
    </ul>
  </div>

  <div class="hex-row">
    <div class="photo" style="left:58px" role="img" aria-label="Photo of two smartphones showing a security control app">
      <svg viewBox="0 0 116 132"><polygon points="58,3 113,35 113,97 58,129 3,97 3,35" fill="url(#g-app)" stroke="#111" stroke-width="4"/><polyline points="3,55 3,35 58,3 113,35 113,55" fill="none" stroke="#f15a22" stroke-width="5"/></svg>
    </div>
    <span class="hex-shadow" style="left:71px"></span>
    <div class="photo" style="left:194px" role="img" aria-label="Photo of a finger pressing an alarm keypad">
      <svg viewBox="0 0 116 132"><polygon points="58,3 113,35 113,97 58,129 3,97 3,35" fill="url(#g-keypad)" stroke="#111" stroke-width="4"/><polyline points="3,55 3,35 58,3 113,35 113,55" fill="none" stroke="#f15a22" stroke-width="5"/></svg>
    </div>
    <span class="hex-shadow" style="left:207px"></span>
    <div class="photo" style="left:330px" role="img" aria-label="Photo of a wall-mounted touchscreen alarm panel">
      <svg viewBox="0 0 116 132"><polygon points="58,3 113,35 113,97 58,129 3,97 3,35" fill="url(#g-app)" stroke="#111" stroke-width="4"/><polyline points="3,55 3,35 58,3 113,35 113,55" fill="none" stroke="#f15a22" stroke-width="5"/></svg>
    </div>
    <span class="hex-shadow" style="left:343px"></span>
  </div>

  <p class="back-body">With the new cloud-based system we can check the alarm performance anytime you need it. This gives us the capability to assist you in any of your needs, be that changing user codes or system configuration. We are always there, working in the background to make sure you have the support and help you need. This is taking alarm systems into the future and leaving the stand-alone systems in the past.</p>

  <div class="promise-band">R J Security Systems are always there, always available,<br>wherever and whenever you need us.</div>

  <div class="contact-bar">
    <span class="contact-bar__icon"><svg viewBox="0 0 20 20"><path d="M12.5 5.5c-2.5-.5-5 1.8-5 4.5s2.5 5 5 4.5l-.6-2.4c-1.2.1-2.1-.9-2.1-2.1s.9-2.2 2.1-2.1z" fill="#fff"/></svg></span>
    <p class="contact-bar__phone">01632 960482</p>
    <ul class="contact-bar__details">
      <li>14 Harbour Lane, Marston, Essex, CM99 2ZX</li>
      <li>operations@rjsecuritysystems.co.uk</li>
      <li>www.rjsecuritysystems.co.uk</li>
    </ul>
  </div>
</section>

<p class="side-label side-label--front">FRONT</p>
<p class="side-label side-label--back">BACK</p>
<p class="board-caption">R J SECURITY FLYER - SECURITY BASED COMPANY</p>

</body>
</html>
```